Design Packaging Cover For Brisk 4 Ergonomic Seat Cushion

We need a new front cover for our Brisk 4 Seat Cushion package. Insert cover will be placed on top of the cushion under a clear plastic wrap.

Brisk 4 is an online retailer of pain relief solutions and ergonomic products that make life easier and more comfortable.

Our name Brisk 4 means a state of bliss, elation or happiness. We would like an eye-catching design that capitalizes on the popularity of the term “On Brisk 4” by selling the emotion of contented happiness that comes from owning our products. Our products improve the lives of our customers and we will market that by creating experiences that are memorable and keep people coming back.
Take a look at our website for inspiration. Brisk4SeatCushion.com

```html
<!DOCTYPE html>
<html lang="en">
<head>
<meta charset="utf-8">
<title>Brisk 4 Seat Cushion – Package Cover</title>
<link href="https://fonts.googleapis.com/css2?family=Montserrat:ital,wght@0,600;0,700;0,800;1,800&family=Mulish:wght@400;500;700&display=swap" rel="stylesheet">
<style>
  :root {
    --brand-blue: #1b72b9;
    --sky-blue: #2a9fdc;
    --sky-deep: #3f86c6;
    --ink: #111111;
    --text: #222222;
    --muted: #3a3a3a;
    --white: #ffffff;
    --badge-yellow: #f5b41a;
    --page: #f2f2f2;
  }
  * { margin: 0; padding: 0; box-sizing: border-box; }
  html, body { width: 929px; height: 1200px; overflow: hidden; background: var(--page); }
  .stage { position: relative; width: 929px; height: 1200px; }
  .cover {
    position: absolute; left: 20px; top: 256px;
    width: 1312px; height: 1014px;
    transform: scale(0.6776); transform-origin: 0 0;
    background: var(--white); overflow: hidden;
    box-shadow: 0 14px 40px rgba(0,0,0,.28);
    font-family: "Mulish", sans-serif; color: var(--text);
  }
  .sky {
    position: absolute; left: 0; top: 256px; width: 1312px; height: 520px;
    background: linear-gradient(180deg, var(--sky-deep) 0%, #5a9bd3 22%, #b9d6ef 42%, #ffffff 62%);
  }
  .logo-tab { position: absolute; left: 96px; top: 0; width: 262px; height: 312px; }
  .logo-tab .brand-name {
    position: absolute; left: 0; top: 120px; width: 262px; text-align: center;
    font-family: "Montserrat", sans-serif; font-weight: 700; font-size: 48px; color: var(--white);
  }
  .logo-tab .brand-dot {
    position: absolute; left: 115px; top: 70px; width: 32px; height: 32px;
    border-radius: 50%; border: 4px solid var(--white);
  }
  .title { position: absolute; right: 50px; top: 40px; text-align: right; color: var(--brand-blue); font-family: "Montserrat", sans-serif; }
  .title .kicker { font-weight: 700; font-size: 55px; letter-spacing: 1px; line-height: 1; }
  .title .main { font-weight: 800; font-size: 96px; line-height: 1; margin-top: 4px; letter-spacing: -1px; }
  .title .sub { font-family: "Mulish", sans-serif; font-weight: 500; font-size: 37px; line-height: 1.1; margin-top: 2px; }
  .banner { position: absolute; left: 0; top: 422px; width: 850px; height: 54px; }
  .banner span {
    position: absolute; left: 48px; top: 10px;
    font-family: "Montserrat", sans-serif; font-weight: 800; font-style: italic;
    font-size: 27px; color: var(--white); letter-spacing: .3px; white-space: nowrap;
  }
  .benefits { position: absolute; left: 86px; top: 507px; list-style: none; }
  .benefits li { font-size: 24px; line-height: 38px; display: flex; align-items: center; color: var(--text); white-space: nowrap; }
  .benefits li svg { width: 20px; height: 20px; margin-right: 10px; }
  .features { position: absolute; left: 56px; top: 705px; display: flex; }
  .feature { width: 153px; text-align: center; }
  .feature svg { height: 70px; width: 90px; display: block; margin: 0 auto 16px; }
  .feature h3 { font-family: "Montserrat", sans-serif; font-weight: 700; font-size: 11px; color: var(--ink); margin-bottom: 12px; white-space: nowrap; }
  .feature p { font-size: 10.5px; line-height: 13px; color: var(--muted); padding: 0 4px; }
  .photo-model {
    position: absolute; left: 830px; top: 445px; width: 482px; height: 420px;
    background: radial-gradient(ellipse at 55% 45%, #e8d6cb 0%, #d9d5d2 38%, rgba(235,238,242,0) 72%);
  }
  .photo-cushion {
    position: absolute; left: 775px; top: 700px; width: 300px; height: 215px;
    border-radius: 40px 30px 60px 70px;
    background: linear-gradient(110deg, #141414 0%, #232323 55%, #4aa3dc 62%, #8ccbef 85%, #e9f2f8 100%);
  }
  .bottom-art { position: absolute; left: 0; top: 0; width: 1312px; height: 1014px; }
  .badge { position: absolute; left: 1050px; top: 727px; width: 160px; height: 160px; border-radius: 50%; background: var(--badge-yellow); border: 6px solid var(--white); }
  .badge .badge-card {
    position: absolute; left: 19px; top: 32px; width: 110px; height: 84px;
    background: var(--brand-blue); border: 3px solid var(--white); transform: rotate(-6deg);
    color: var(--white); text-align: center; font-family: "Montserrat", sans-serif;
    display: flex; flex-direction: column; justify-content: center; line-height: 1.1;
    white-space: nowrap;
  }
  .badge-card .b1 { font-size: 12px; font-weight: 600; }
  .badge-card .b2 { font-size: 16px; font-weight: 800; }
  .badge-card .b3 { font-size: 12px; font-weight: 600; }
  .url {
    position: absolute; left: 84px; top: 960px;
    font-size: 31px; color: var(--white); letter-spacing: 1px; font-weight: 500; white-space: nowrap;
  }
  .uses { position: absolute; left: 840px; top: 908px; display: flex; }
  .use { width: 87.5px; text-align: center; }
  .use .circle { width: 58px; height: 58px; border-radius: 50%; background: var(--brand-blue); margin: 0 auto; display: flex; align-items: center; justify-content: center; }
  .use .circle svg { width: 34px; height: 34px; }
  .use span { display: block; margin-top: 12px; font-family: "Montserrat", sans-serif; font-weight: 600; font-size: 8.5px; color: var(--white); letter-spacing: .3px; white-space: nowrap; }
</style>
</head>
<body>
<div class="stage">
  <div class="cover">
    <div class="sky" role="img" aria-label="Photograph of white clouds against a blue sky"></div>

    <div class="logo-tab">
      <svg width="262" height="312" viewBox="0 0 262 312">
        <path d="M0 0 H262 V288 Q131 318 0 288 Z" fill="#111111"/>
      </svg>
      <div class="brand-dot"></div>
      <div class="brand-name">Brisk 4</div>
    </div>

    <div class="title">
      <div class="kicker">THERAPEUTIC</div>
      <div class="main">SEAT CUSHION</div>
      <div class="sub">With Float-Lite™ Comfort Gel</div>
    </div>

    <div class="banner">
      <svg width="850" height="54" viewBox="0 0 850 54"><polygon points="0,0 850,0 800,54 0,54" fill="#1b72b9"/></svg>
      <span>ERGONOMIC DESIGN FOR CLOUD-LIKE COMFORT</span>
    </div>

    <ul class="benefits">
      <li><svg viewBox="0 0 20 20"><path d="M7 0h6v7h7v6h-7v7H7v-7H0V7h7z" fill="#1b72b9"/></svg>Back Pain &amp; Sciatica Relief</li>
      <li><svg viewBox="0 0 20 20"><path d="M7 0h6v7h7v6h-7v7H7v-7H0V7h7z" fill="#1b72b9"/></svg>Promotes Healthy Posture</li>
      <li><svg viewBox="0 0 20 20"><path d="M7 0h6v7h7v6h-7v7H7v-7H0V7h7z" fill="#1b72b9"/></svg>Eliminates Pressure Points</li>
      <li><svg viewBox="0 0 20 20"><path d="M7 0h6v7h7v6h-7v7H7v-7H0V7h7z" fill="#1b72b9"/></svg>Improve Blood Circulation</li>
      <li><svg viewBox="0 0 20 20"><path d="M7 0h6v7h7v6h-7v7H7v-7H0V7h7z" fill="#1b72b9"/></svg>Relieves Stress &amp; Boost Energy</li>
    </ul>

    <div class="features">
      <div class="feature">
        <svg viewBox="0 0 90 70"><path d="M14 56 Q2 56 4 44 Q6 34 18 36 Q18 22 32 22 Q38 8 52 12 Q64 14 64 28 Q78 26 82 38 Q88 54 72 56 Z" fill="none" stroke="#1b72b9" stroke-width="2"/></svg>
        <h3>Cloud-Like Comfort</h3>
        <p>Advanced orthopedic design evenly distributes body weight, thereby preventing pressure points for back pain relief.</p>
      </div>
      <div class="feature">
        <svg viewBox="0 0 90 70"><g fill="none" stroke="#1b72b9" stroke-width="2"><path d="M30 10 Q22 30 30 60"/><path d="M60 6 Q70 28 60 58"/><path d="M40 12 L44 56 M50 10 L48 56"/><path d="M36 22 h20 M35 32 h22 M35 42 h22"/><path d="M18 46 l8 4 M16 54 l10 0 M20 62 l6 -4"/></g></svg>
        <h3>Pressure Relief</h3>
        <p>Special U-shape Cutout eliminates contact pressure on the tailbone, preventing sciatica and lower back pain.</p>
      </div>
      <div class="feature">
        <svg viewBox="0 0 90 70"><g fill="none" stroke="#1b72b9" stroke-width="2"><path d="M16 14 Q40 6 60 14 Q76 18 80 26 Q60 28 40 26 Q20 24 16 14 Z"/><rect x="8" y="36" width="76" height="24" rx="12"/></g><g fill="#1b72b9"><circle cx="20" cy="44" r="2.5"/><circle cx="30" cy="44" r="2.5"/><circle cx="40" cy="44" r="2.5"/><circle cx="50" cy="44" r="2.5"/><circle cx="60" cy="44" r="2.5"/><circle cx="70" cy="44" r="2.5"/><circle cx="25" cy="52" r="2.5"/><circle cx="35" cy="52" r="2.5"/><circle cx="45" cy="52" r="2.5"/><circle cx="55" cy="52" r="2.5"/><circle cx="65" cy="52" r="2.5"/></g></svg>
        <h3>Float-Lite™ Comfort Gel</h3>
        <p>A soothing top layer of cushioning gel microbeads provides extra support and creates the sensation of sitting on air as it adds bounce, lift and coolness..</p>
      </div>
      <div class="feature">
        <svg viewBox="0 0 90 70"><g fill="none" stroke="#1b72b9" stroke-width="2"><path d="M30 4 Q24 34 32 68"/><path d="M60 4 Q66 34 58 68"/><rect x="40" y="8" width="10" height="8" rx="2"/><rect x="40" y="20" width="10" height="8" rx="2"/><rect x="40" y="32" width="10" height="8" rx="2"/><rect x="40" y="44" width="10" height="8" rx="2"/><rect x="40" y="56" width="10" height="8" rx="2"/></g></svg>
        <h3>Promotes Good Posture</h3>
        <p>Ergonomic contoured shape conforms to the shape of your body helping to place your back in correct alignment, providing long lasting pain relief.</p>
      </div>
    </div>

    <div class="photo-model" role="img" aria-label="Photograph of a smiling woman in a white blouse relaxing with hands behind her head"></div>

    <svg class="bottom-art" viewBox="0 0 1312 1014">
      <polygon points="0,940 770,940 570,1014 0,1014" fill="#111111"/>
      <polygon points="1312,760 1312,1014 580,1014" fill="#2a9fdc"/>
      <polygon points="1312,760 1312,800 700,1014 580,1014" fill="#1b72b9" opacity=".5"/>
    </svg>

    <div class="photo-cushion" role="img" aria-label="Product photograph of the black contoured seat cushion with blue gel layer"></div>

    <div class="badge">
      <div class="badge-card"><span class="b1">Featuring</span><span class="b2">Float-Lite</span><span class="b3">Comfort Gel</span></div>
    </div>

    <div class="url">WWW.BRISK4SEATCUSHION.COM</div>

    <div class="uses">
      <div class="use"><div class="circle"><svg viewBox="0 0 34 34" fill="#fff"><rect x="11" y="3" width="12" height="13" rx="3"/><rect x="8" y="17" width="18" height="4" rx="2"/><rect x="16" y="21" width="2" height="6"/><path d="M9 29 h16 v2 H9z"/></svg></div><span>OFFICE CHAIRS</span></div>
      <div class="use"><div class="circle"><svg viewBox="0 0 34 34" fill="#fff"><rect x="9" y="4" width="16" height="10" rx="1"/><rect x="7" y="16" width="20" height="4"/><rect x="8" y="20" width="3" height="11"/><rect x="23" y="20" width="3" height="11"/></svg></div><span>HOME CHAIRS</span></div>
      <div class="use"><div class="circle"><svg viewBox="0 0 34 34"><g fill="none" stroke="#fff" stroke-width="2.4"><circle cx="14" cy="22" r="8"/><path d="M10 4 V16 H22 L26 26 H30"/></g><circle cx="26" cy="30" r="2" fill="#fff"/></svg></div><span>WHEEL CHAIRS</span></div>
      <div class="use"><div class="circle"><svg viewBox="0 0 34 34" fill="#fff"><path d="M6 16 L10 8 H24 L28 16 V25 H6 Z"/><rect x="7" y="25" width="5" height="4"/><rect x="22" y="25" width="5" height="4"/><circle cx="11" cy="19" r="2" fill="#1b72b9"/><circle cx="23" cy="19" r="2" fill="#1b72b9"/></svg></div><span>CARS</span></div>
      <div class="use"><div class="circle"><svg viewBox="0 0 34 34"><circle cx="15" cy="19" r="11" fill="none" stroke="#fff" stroke-width="2.4"/><path d="M20 12 L31 3 L28 9 Z" fill="#fff"/></svg></div><span>TRAVEL</span></div>
    </div>
  </div>
</div>
</body>
</html>
```